Commercial Construction Company

We need a business card design based on our current logo. We are a commercial general contractor based in Southern California that specializes in bank remodels. We would like to see designs that incorporate dark blue. The final design should portray an image of professionalism and quality.

If possible, I would like to add metallic foil to the design. Thank you

```html
<!DOCTYPE html>
<html lang="en">
<head>
<meta charset="utf-8">
<title>Halvern Commercial Building Services – Business Card</title>
<link rel="stylesheet" href="https://fonts.googleapis.com/css2?family=Archivo:wght@800&display=swap">
<style>
  :root {
    --backdrop: #e6e8ea;
    --navy: #0d4488;
    --deep-navy: #0a2f7a;
    --royal: #1560d8;
    --bright-blue: #2a8cff;
    --steel-blue: #0f7fc4;
    --cyan: #19f5ff;
    --panel-light: #f4f6f8;
    --panel-shade: #c9d6e3;
    --ink: #161616;
    --mark-blue: #2f6aa6;
  }
  html, body {
    margin: 0;
    padding: 0;
    width: 1200px;
    height: 900px;
    overflow: hidden;
    background: var(--backdrop);
  }
  .stage {
    width: 1200px;
    height: 900px;
    display: flex;
    align-items: center;
    justify-content: center;
  }
  .card {
    position: relative;
    width: 1050px;
    height: 600px;
    box-shadow: 0 10px 30px rgba(0, 0, 0, 0.18);
    overflow: hidden;
  }
  .card-art {
    position: absolute;
    inset: 0;
    width: 100%;
    height: 100%;
  }
  .brand {
    position: absolute;
    left: 330px;
    top: 175px;
    display: flex;
    align-items: center;
    gap: 24px;
  }
  .brand-dot {
    width: 56px;
    height: 56px;
    border-radius: 50%;
    background: var(--mark-blue);
    flex: none;
  }
  .brand-name {
    margin: 0;
    font-family: "Archivo", sans-serif;
    font-weight: 800;
    font-size: 42px;
    line-height: 1.15;
    color: var(--ink);
  }
</style>
</head>
<body>
<main class="stage">
  <section class="card" aria-label="Business card front">
    <svg class="card-art" viewBox="0 0 1050 600" aria-hidden="true">
      <defs>
        <linearGradient id="panelGradient" x1="0" y1="0" x2="1" y2="1">
          <stop offset="0" stop-color="var(--panel-light)"/>
          <stop offset="1" stop-color="var(--panel-shade)"/>
        </linearGradient>
        <linearGradient id="cyanGlow" x1="0" y1="0" x2="1" y2="1">
          <stop offset="0" stop-color="var(--cyan)"/>
          <stop offset="1" stop-color="var(--steel-blue)"/>
        </linearGradient>
      </defs>

      <rect class="base-band" width="1050" height="600" fill="var(--navy)"/>

      <polygon class="left-glow" points="0,0 200,0 120,600 0,600" fill="url(#cyanGlow)"/>
      <polygon class="left-stripe" points="200,0 250,0 170,600 120,600" fill="var(--steel-blue)"/>
      <polygon class="left-stripe-thin" points="250,0 262,0 182,600 170,600" fill="var(--bright-blue)"/>

      <polygon class="right-stripe" points="890,0 930,0 980,600 940,600" fill="var(--deep-navy)"/>
      <polygon class="right-stripe" points="930,0 965,0 1015,600 980,600" fill="var(--royal)"/>
      <polygon class="right-stripe" points="965,0 985,0 1035,600 1015,600" fill="var(--bright-blue)"/>
      <polygon class="right-stripe" points="985,0 1050,0 1050,600 1035,600" fill="var(--royal)"/>

      <polygon class="light-panel" points="262,0 880,0 960,290 790,470 200,470" fill="url(#panelGradient)"/>
    </svg>

    <div class="brand">
      <span class="brand-dot" aria-hidden="true"></span>
      <p class="brand-name">Halvern Commercial<br>Building Services</p>
    </div>
  </section>
</main>
</body>
</html>
```